Flyer-Design für nachhaltige Spülbecher aus Keramik
Zielgruppe
Zielgruppe des Flyers sind Zahnärzte. Wir fertigen die ersten nachhaltigen Spülbecher für Praxen aus Keramik.
Aufgabenstellung
Der Flyer soll einen hochwertigen und exklusiven Eindruck hinterlassen.
Auf dem Flyer sollte das Logo, Kontaktmöglichkeiten, Anschrift, 1-2 Bilder des Produktes und ein kleiner Text bezüglich Nachhaltigkeit vorhanden sein. Die aktuell hochgeladenen Bilder der Becher sind aktuell noch Platzhalter, es werden in den nächsten Tagen die richtigen Bilder hochgeladen.
WICHTIG: Bitte einen Platzhalter für eine Überschrift und Stichpunkte/Informationen einarbeiten. Leider ist noch nicht Final klar wir diese Lauten soll, daher wird dieser Teil noch von mir noch selbst ergänzt. Danke
Website: www.lindgau-keramik.de

```html
<!DOCTYPE html>
<html lang="de">
<head>
<meta charset="utf-8">
<title>Lindgau Keramik – Flyer</title>
<link href="https://fonts.googleapis.com/css2?family=Old+Standard+TT:wght@700&family=Cabin:wght@400&family=Montserrat:wght@600&display=swap" rel="stylesheet">
<style>
  :root {
    --backdrop: #ececec;
    --grey: #9b9b9b;
    --navy: #12305a;
    --navy-deep: #0b2347;
    --teal: #21597c;
    --white: #ffffff;
    --ink: #1a1f2b;
  }
  * { box-sizing: border-box; margin: 0; padding: 0; }
  html, body {
    width: 1200px; height: 800px; overflow: hidden;
    background: var(--backdrop);
  }
  .canvas { position: relative; width: 1200px; height: 800px; }
  .page {
    position: absolute; top: 158px; width: 342px; height: 484px;
    overflow: hidden; background: var(--navy-deep);
    box-shadow: 0 1px 3px rgba(0,0,0,.15);
  }
  .page--front { left: 242px; }
  .page--back { left: 616px; }
  .block { position: absolute; }
  .block--grey { background: var(--grey); }
  .block--navy { background: var(--navy); }
  .block--deep { background: var(--navy-deep); }
  .block--teal { background: var(--teal); }
  .block--white { background: var(--white); }

  .headline {
    position: absolute; color: #eeeeee;
    font-family: "Old Standard TT", serif; font-weight: 700;
    line-height: 1.02;
  }
  .brand {
    position: absolute; text-align: center; color: var(--white);
    font-family: "Montserrat", sans-serif; font-weight: 600; font-size: 9px;
  }
  .brand__mark {
    display: block; width: 34px; height: 30px; margin: 0 auto 10px;
    border: 1.2px solid var(--white);
  }
  .body-text {
    position: absolute; color: var(--white);
    font-family: "Cabin", sans-serif; font-size: 9px; line-height: 1.55;
  }
  .subhead {
    position: absolute; color: #eeeeee;
    font-family: "Old Standard TT", serif; font-weight: 700; font-size: 16px;
  }
  .url {
    position: absolute; color: var(--white);
    font-family: "Cabin", sans-serif; font-size: 10px; letter-spacing: -0.02em;
  }
  .tagline {
    position: absolute; color: var(--ink);
    font-family: "Cabin", sans-serif; font-size: 16px; letter-spacing: 0.3em;
  }
  .photo { position: absolute; }
  .photo--cups-row { background: linear-gradient(100deg, #1f4a72 0%, #b56a6e 45%, #d9d3c9 85%, #15243a 100%); }
  .photo--mug { background: linear-gradient(180deg, #2c4b6a 0%, #8d96a6 30%, #6a6d7c 65%, #d8d8d4 100%); }
  .photo--cups-stack { background: linear-gradient(160deg, #2a6a92 0%, #6d9bb5 45%, #9aa8b0 75%, #a77a8d 100%); }
  .photo--hands { background: radial-gradient(circle at 45% 50%, #d8d3cb 0%, #a9acb3 40%, #5f6674 80%, #8a93a0 100%); }
  .photo--forest { background: linear-gradient(180deg, #2f4c5e 0%, #4f6e78 55%, #3f6b57 100%); }
</style>
</head>
<body>
<main class="canvas">

  <section class="page page--front" aria-label="Flyer Vorderseite">
    <div class="block block--grey" style="left:0;top:0;width:198px;height:143px"></div>
    <h1 class="headline" style="left:20px;top:42px;font-size:37px">Lindgau<br>Keramik</h1>
    <div class="block block--navy" style="left:198px;top:0;width:95px;height:143px"></div>
    <div class="block block--teal" style="left:293px;top:0;width:49px;height:143px"></div>
    <div class="brand" style="left:198px;top:44px;width:144px">
      <span class="brand__mark"></span>Lindgau Keramik GmbH
    </div>

    <div class="photo photo--cups-row" role="img" aria-label="Foto: Reihe farbiger Keramik-Spülbecher" style="left:0;top:143px;width:198px;height:176px"></div>
    <p class="body-text" style="left:8px;top:280px;width:188px;font-size:9.3px">Lorem ipsum dolor sit amet, consectetuer adipiscing elit, sed diam nonummy nibh euismod tincidunt ut laoreet dolore magna</p>

    <div class="photo photo--mug" role="img" aria-label="Foto: grauer Keramikbecher unter Wasserhahn" style="left:198px;top:143px;width:144px;height:233px"></div>

    <div class="block block--deep" style="left:0;top:319px;width:126px;height:165px"></div>
    <h2 class="subhead" style="left:9px;top:348px">Kontakt</h2>
    <p class="body-text" style="left:9px;top:372px;width:112px">Lorem ipsum dolor sit amet, consectetuer adipiscing elit, sed diam nonummy nibh euismod</p>
    <p class="url" style="left:8px;top:463px">www.lindgau-keramik.de</p>

    <div class="photo photo--cups-stack" role="img" aria-label="Foto: gestapelte Keramikbecher" style="left:126px;top:319px;width:72px;height:165px"></div>

    <div class="block block--deep" style="left:198px;top:376px;width:144px;height:108px"></div>
    <p class="body-text" style="left:214px;top:410px;width:124px">Lorem ipsum dolor sit amet, consectetuer adipiscing elit, sed diam nonummy nibh euismod</p>
  </section>

  <section class="page page--back" aria-label="Flyer Rückseite">
    <div class="block block--grey" style="left:0;top:0;width:192px;height:139px"></div>
    <h2 class="headline" style="left:17px;top:50px;font-size:42px">Qualität</h2>
    <div class="block block--navy" style="left:192px;top:0;width:96px;height:139px"></div>
    <div class="block block--teal" style="left:288px;top:0;width:54px;height:139px"></div>
    <div class="brand" style="left:192px;top:38px;width:150px">
      <span class="brand__mark"></span>Lindgau Keramik GmbH
    </div>

    <div class="photo photo--hands" role="img" aria-label="Foto: Hände formen Ton auf der Töpferscheibe" style="left:0;top:139px;width:281px;height:282px"></div>
    <div class="photo photo--forest" role="img" aria-label="Foto: nebliger Nadelwald" style="left:281px;top:139px;width:61px;height:238px"></div>
    <div class="block block--deep" style="left:281px;top:377px;width:61px;height:44px"></div>

    <div class="block block--white" style="left:0;top:421px;width:196px;height:63px"></div>
    <p class="tagline" style="left:16px;top:442px">Nachhaltigkeit</p>
    <div class="block block--deep" style="left:196px;top:421px;width:146px;height:63px"></div>
    <p class="body-text" style="left:210px;top:432px;width:128px">Lorem ipsum dolor sit amet, consectetuer adipiscing elit, sed diam nonummy nibh euismod</p>
  </section>

</main>
</body>
</html>
```